Website design for staffing/workforce solutions company - Harbor Crest Solutions

Create a launch-ready website
Harbor Crest Solutions also known as HCS. This is a company that specializes in Staffing/Work force solutions for Healthcare/IT/Logistics/Maintenance/Construction/Manufacturing/Industrial/General Labor. HCS works with government agencies/contracts also. Use the attached logo in the build of the website. Website should be clean, modern, engaging, innovative. Website needs to speak to the professional services industry.
Harbor Crest Solutions or HCS is a certified VOSB, SDVOSB, DBE and Minority-Owned Business.
The website needs to be compliant for government contracting.

Website needs to include the following--
Modern UI/UX Enhancements: A hero section with a strong call-to-action.
Government Contracting Compliance: Certification display and a Capability Statement download.
Advanced Careers Section: A dedicated job application portal.
Social Media & Lead Generation: Links to Workvine, Quillo, and Pagebloom.
Security & Performance: Optimized for SEO, fast loading, and mobile responsiveness.
1. Modern Design Upgrades
๐Ÿ”น Upgrade UI/UX for a Professional, Trustworthy Look
โœ… Full-width hero banner with a high-quality background image representing business, technology, and workforce solutions.
โœ… Animated elements (subtle transitions for smooth browsing experience).
โœ… Bold CTA buttons for easy navigation to key actions (e.g., โ€œGet Startedโ€ or โ€œRequest a Consultationโ€).
โœ… Dark-themed header with contrasting colors (professional & government-trustworthy).
โœ… New Homepage Hero Section Example:
"Your Trusted Partner in Workforce, IT, Maintenance & Logistics Solutions"
Button: "Discover Our Services"

2. Enhanced Government Contracting Section (Key for Compliance)
๐Ÿ“Œ Essential for securing contracts & building credibility
โœ… Capability Statement (Downloadable PDF)

Showcase key past contracts, company qualifications, and services in a downloadable format for government buyers.
โœ… Certifications Display (VOSB, SDVOSB, DBE, Minority-Owned Business)

Visual badge display to emphasize legitimacy for government contracts.
โœ… Procurement Readiness Details

NAICS Codes, DUNS Number, CAGE Code, and relevant KPR.example registration details.
โœ… Past Performance Showcase (Case Studies Section)

Highlight successful projects and government contracts.
โœ… Compliance & Security

Add SOC 2, HIPAA (for healthcare staffing), and ITAR compliance if applicable.
3. Advanced Job Search & Candidate Portal (For Staffing Services)
๐Ÿ“Œ To attract top talent for staffing contracts

โœ… Advanced Job Search Feature

Filters: Industry, location, job type (contract/full-time), salary range, and clearance level (for government jobs).
โœ… Candidate Login Portal

Applicants can upload resumes, track applications, and receive job alerts.
โœ… Employer Portal (For Businesses Hiring Through HCS)

A dedicated section for companies to submit staffing requests and view candidate matches.
4. Service-Specific Landing Pages (SEO & Engagement)
๐Ÿ“Œ Helps different industries find relevant services faster

๐Ÿ”น Dedicated Pages for Each Service:
โœ… Staffing & Workforce Solutions

Specialized sections for Healthcare, IT, Construction, Industrial, and General Labor staffing.
โœ… IT Services

List services like Cybersecurity, Cloud Solutions, and IT Consulting.
Showcase tech stack & certifications.
โœ… Logistics & Maintenance

Detail fleet management, supply chain services, and industrial maintenance.
โœ… Government Contracting Solutions

A streamlined page for government agencies.
5. Security & Compliance Upgrades (For Government Work)
๐Ÿ“Œ To ensure compliance & credibility in government contracting

โœ… SSL Certification (100% Required for Security)

Secure client and job applicant data.
โœ… ADA Compliance (Accessibility)

Ensure the website follows WCAG 2.1 accessibility standards for government clients.
โœ… GDPR & Data Protection Features

A privacy policy and terms of service to comply with data regulations.
6. Performance & Mobile Optimization
๐Ÿ“Œ To ensure fast loading & responsiveness

โœ… Mobile-Responsive Design

Optimized for mobile-friendly navigation since many users browse from phones.
โœ… Fast-Loading Pages

Optimize images & implement lazy loading for better site speed.
โœ… SEO-Optimized Pages

Improve search ranking on Findoro with:
Keyword-optimized content (e.g., โ€œGovernment Contracting Staffing Servicesโ€)
Schema markup for job listings
Blog/articles about staffing trends
7. Social Media & Lead Generation
๐Ÿ“Œ For brand credibility & client engagement

โœ… Workvine, Quillo, Pagebloom Integration

Display recent updates from Workvine (primary for B2B & government).
โœ… Lead Capture Forms

Forms for business inquiries, talent applications, and government RFPs.
โœ… Client & Candidate Testimonials
Showcase client success stories & employee experiences

Good websites to pull examples for inspiration/direction--
https://www.vlmn.example/
https://www.torvana.example/
https://brightmeridian.example/homepage/
https://www.valdorcheck.example/capability-statement

Industry/Entity Type

Staffing/Professional Services

Coding

Coded - Design and coding required

Number of Pages Required

5+ page

Requirements
Must have
• Website needs to include the following-- Modern UI/UX Enhancements: A hero section with a strong call-to-action. Government Contracting Compliance: Certification display and a Capability Statement download. Advanced Careers Section: A dedicated job application portal. Social Media & Lead Generation: Links to Workvine, Quillo, and Pagebloom. Security & Performance: Optimized for SEO, fast loading, and mobile responsiveness. 1. Modern Design Upgrades ๐Ÿ”น Upgrade UI/UX for a Professional, Trustworthy Look โœ… Full-width hero banner with a high-quality background image representing business, technology, and workforce solutions. โœ… Animated elements (subtle transitions for smooth browsing experience). โœ… Bold CTA buttons for easy navigation to key actions (e.g., โ€œGet Startedโ€ or โ€œRequest a Consultationโ€). โœ… Dark-themed header with contrasting colors (professional & government-trustworthy). โœ… New Homepage Hero Section Example: "Your Trusted Partner in Workforce, IT, & Logistics Solutions" Button: "Discover Our Services" 2. Enhanced Government Contracting Section (Key for Compliance) ๐Ÿ“Œ Essential for securing contracts & building credibility โœ… Capability Statement (Downloadable PDF) Showcase key past contracts, company qualifications, and services in a downloadable format for government buyers. โœ… Certifications Display (VOSB, SDVOSB, DBE, Minority-Owned Business) Visual badge display to emphasize legitimacy for government contracts. โœ… Procurement Readiness Details NAICS Codes, DUNS Number, CAGE Code, and relevant KPR.example registration details. โœ… Past Performance Showcase (Case Studies Section) Highlight successful projects and government contracts. โœ… Compliance & Security Add SOC 2, HIPAA (for healthcare staffing), and ITAR compliance if applicable. 3. Advanced Job Search & Candidate Portal (For Staffing Services) ๐Ÿ“Œ To attract top talent for staffing contracts โœ… Advanced Job Search Feature Filters: Industry, location, job type (contract/full-time), salary range, and clearance level (for government jobs). โœ… Candidate Login Portal Applicants can upload resumes, track applications, and receive job alerts. โœ… Employer Portal (For Businesses Hiring Through HCS) A dedicated section for companies to submit staffing requests and view candidate matches. 4. Service-Specific Landing Pages (SEO & Engagement) ๐Ÿ“Œ Helps different industries find relevant services faster ๐Ÿ”น Dedicated Pages for Each Service: โœ… Staffing & Workforce Solutions Specialized sections for Healthcare, IT, Construction, Industrial, and General Labor staffing. โœ… IT Services List services like Cybersecurity, Cloud Solutions, and IT Consulting. Showcase tech stack & certifications. โœ… Logistics & Maintenance Detail fleet management, supply chain services, and industrial maintenance. โœ… Government Contracting Solutions A streamlined page for government agencies. 5. Security & Compliance Upgrades (For Government Work) ๐Ÿ“Œ To ensure compliance & credibility in government contracting โœ… SSL Certification (100% Required for Security) Secure client and job applicant data. โœ… ADA Compliance (Accessibility) Ensure the website follows WCAG 2.1 accessibility standards for government clients. โœ… GDPR & Data Protection Features A privacy policy and terms of service to comply with data regulations. 6. Performance & Mobile Optimization ๐Ÿ“Œ To ensure fast loading & responsiveness โœ… Mobile-Responsive Design Optimized for mobile-friendly navigation since many users browse from phones. โœ… Fast-Loading Pages Optimize images & implement lazy loading for better site speed. โœ… SEO-Optimized Pages Improve search ranking on Findoro with: Keyword-optimized content (e.g., โ€œGovernment Contracting Staffing Servicesโ€) Schema markup for job listings Blog/articles about staffing trends 7. Social Media & Lead Generation ๐Ÿ“Œ For brand credibility & client engagement โœ… Workvine, Quillo, Pagebloom Integration Display recent updates from Workvine (primary for B2B & government). โœ… Lead Capture Forms Forms for business inquiries, talent applications, and government RFPs. โœ… Client & Candidate Testimonials Showcase client success stories & employee experiences Good websites to pull examples for inspiration/direction-- https://www.vlmn.example/ https://www.torvana.example/ https://brightmeridian.example/homepage/

```html
<!DOCTYPE html>
<html lang="en">
<head>
<meta charset="utf-8">
<title>Harbor Crest Solutions — Workforce Solutions</title>
<link href="https://fonts.googleapis.com/css2?family=Inter:wght@400;500;600;700;800&display=swap" rel="stylesheet">
<style>
:root{
  --navy:#0b1530;--navy2:#13224d;--blue:#2563eb;--blue-d:#1d4ed8;--sky:#60a5fa;
  --ink:#111827;--muted:#6b7280;--line:#e5e7eb;--soft:#f5f7fb;--green:#22c55e;--red:#dc2626;
}
*{box-sizing:border-box;margin:0;padding:0}
html,body{width:1200px;height:5314px;overflow:hidden}
body{font-family:"Inter",sans-serif;color:var(--ink);background:#fff;font-size:12px}
.wrap{width:882px;margin:0 auto;position:relative}
svg{display:inline-block;vertical-align:middle}
.ic{width:16px;height:16px;fill:none;stroke:currentColor;stroke-width:1.8;stroke-linecap:round;stroke-linejoin:round}

/* header */
.site-header{height:82px;background:var(--navy)}
.site-header .wrap{display:flex;align-items:center;height:82px;justify-content:space-between}
.brand{color:#fff;font-weight:700;font-size:17px;letter-spacing:.5px;display:flex;align-items:center;gap:8px}
.brand i{width:12px;height:12px;background:var(--blue);display:block}
.nav{display:flex;gap:28px;color:#d1d5db;font-size:12px;margin-left:150px}
.btn{display:inline-flex;align-items:center;gap:6px;border-radius:6px;font-weight:600;font-size:11px;padding:8px 14px;border:0}
.btn-blue{background:var(--blue);color:#fff}
.btn-white{background:#fff;color:var(--blue)}

/* hero */
.hero{height:654px;background:linear-gradient(120deg,#0d1b45 0%,#1a2f7a 55%,#243fa6 100%);position:relative;overflow:hidden;color:#fff}
.hero .wrap{padding-top:96px}
.pill{display:inline-flex;align-items:center;gap:6px;border-radius:20px;padding:6px 14px;font-size:10px}
.hero .pill{background:rgba(255,255,255,.08);border:1px solid rgba(255,255,255,.2);color:#bfdbfe}
.hero h1{font-size:46px;line-height:54px;font-weight:800;margin-top:16px;width:470px}
.hero h1 span{color:var(--sky)}
.hero p.lead{font-size:14px;line-height:23px;color:#cbd5e1;width:420px;margin-top:18px}
.stats{display:flex;gap:56px;margin-top:48px;margin-left:36px}
.stat b{display:block;font-size:22px;color:var(--sky);font-weight:700}
.stat small{font-size:9px;color:#94a3b8}
.hero-cta{display:flex;gap:14px;margin-top:46px}
.hero-card{position:absolute;left:457px;top:242px;width:425px;height:163px;background:rgba(255,255,255,.08);border:1px solid rgba(255,255,255,.15);border-radius:12px;padding:20px 26px}
.hc-head{display:flex;gap:10px;align-items:center}
.hc-icon{width:30px;height:30px;border-radius:6px;background:var(--blue);display:flex;align-items:center;justify-content:center}
.hc-head b{font-size:11px;display:block}.hc-head small{font-size:9px;color:#cbd5e1}
.hc-row{display:flex;justify-content:space-between;font-size:10px;margin-top:14px;color:#e2e8f0}
.hc-row i{width:6px;height:6px;border-radius:50%;background:var(--green);display:block}
.orb{position:absolute;left:1014px;top:320px;width:70px;height:70px;border-radius:50%;background:rgba(96,165,250,.35)}

/* section heads */
.sec-head{text-align:center}
.sec-head h2{font-size:25px;font-weight:700}
.sec-head p{font-size:13px;line-height:21px;color:var(--muted);width:560px;margin:12px auto 0}
.tag{background:#dbeafe;color:var(--blue);border:1px solid #bfdbfe}

/* services */
.services{height:1006px;padding-top:60px}
.svc-grid{display:grid;grid-template-columns:repeat(4,1fr);gap:18px;margin-top:48px}
.svc{border:1px solid var(--line);border-radius:10px;box-shadow:0 2px 8px rgba(0,0,0,.05);padding:22px 18px;text-align:center;height:282px}
.svc.r2{height:266px}
.svc .ico{width:42px;height:42px;border-radius:8px;background:#eff6ff;color:var(--blue);display:flex;align-items:center;justify-content:center;margin:0 auto}
.svc h3{font-size:14px;font-weight:500;margin:20px 0 24px}
.svc p{font-size:10.5px;line-height:17px;color:var(--muted)}
.svc ul{list-style:none;text-align:left;margin-top:10px}
.svc li{font-size:9.5px;color:var(--muted);line-height:20px;padding-left:10px;position:relative}
.svc li:before{content:"";position:absolute;left:0;top:8px;width:4px;height:4px;border-radius:50%;background:var(--blue)}
.gov-banner{margin-top:38px;height:157px;border-radius:12px;background:linear-gradient(90deg,#1d4ed8,#2563eb);color:#fff;text-align:center;padding-top:26px}
.gov-banner h3{font-size:16px;font-weight:700}
.gov-banner p{font-size:11px;line-height:18px;color:#dbeafe;width:500px;margin:10px auto 14px}

/* government */
.gov{height:877px;background:var(--soft);padding-top:64px}
.cert-grid{display:grid;grid-template-columns:repeat(4,1fr);gap:18px;margin-top:40px}
.cert{background:#fff;border:1px solid var(--line);border-radius:10px;height:231px;text-align:center;padding:24px 16px}
.cert .ico{width:44px;height:44px;border-radius:50%;background:#f3f4f6;display:flex;align-items:center;justify-content:center;margin:0 auto;color:#374151}
.badge{display:inline-block;font-size:8px;font-weight:600;border-radius:10px;padding:3px 9px;margin-top:16px}
.b-green{background:#dcfce7;color:#15803d}.b-blue{background:#dbeafe;color:#1d4ed8}.b-purple{background:#ede9fe;color:#6d28d9}.b-orange{background:#ffedd5;color:#c2410c}
.cert h3{font-size:13px;font-weight:500;line-height:20px;margin-top:8px;height:44px}
.cert p{font-size:9.5px;line-height:15px;color:var(--muted);margin-top:22px}
.gov-low{display:flex;gap:35px;margin-top:50px;align-items:flex-start}
.core{width:422px;height:163px;background:#fff;border:1px solid var(--line);border-radius:10px;padding:18px 18px}
.panel-title{display:flex;align-items:center;gap:8px;font-size:11.5px;font-weight:500}
.core-list{display:grid;grid-template-columns:1fr 1fr;gap:4px 10px;margin-top:18px;list-style:none}
.core-list li{font-size:9.5px;color:#374151;line-height:19px;padding-left:10px;position:relative}
.core-list li:before{content:"";position:absolute;left:0;top:7px;width:4px;height:4px;border-radius:50%;background:var(--blue)}
.capab{width:425px;height:286px;background:#eff6ff;border:1px solid #dbeafe;border-radius:10px;padding:18px 18px}
.capab p{font-size:10.5px;line-height:17px;color:#4b5563;margin-top:14px}
.doc{background:#fff;border:1px solid var(--line);border-radius:8px;height:46px;margin-top:12px;display:flex;align-items:center;justify-content:space-between;padding:0 10px}
.doc b{font-size:10.5px;font-weight:500;display:block}.doc small{font-size:8.5px;color:var(--muted)}
.doc .btn{font-size:9px;padding:6px 12px}
.btn-ghost{background:#fff;color:#374151}
.full{display:flex;justify-content:center;width:100%;margin-top:12px;padding:8px}

/* careers */
.careers{height:1130px;padding-top:66px}
.tag-green{background:#fff;color:#16a34a}
.careers-grid{display:flex;gap:29px;margin-top:70px}
.jobs{width:581px}
.search{height:56px;border:1px solid var(--line);border-radius:10px;display:flex;align-items:center;gap:10px;padding:0 14px;box-shadow:0 2px 6px rgba(0,0,0,.04)}
.search .field{flex:1;height:26px;background:#f3f4f6;border-radius:6px;font-size:10px;color:#9ca3af;display:flex;align-items:center;gap:6px;padding:0 10px}
.search .filter{font-size:10px;border:1px solid var(--line);border-radius:6px;padding:6px 12px;display:flex;gap:6px;align-items:center}
.job{height:175px;border:1px solid var(--line);border-radius:10px;margin-top:17px;padding:16px 18px;position:relative;box-shadow:0 2px 6px rgba(0,0,0,.04)}
.job h3{font-size:13px;font-weight:600}
.chips{display:flex;gap:6px;margin-top:6px}
.chip{font-size:7.5px;background:#f3f4f6;border-radius:4px;padding:3px 7px;font-weight:500}
.chip.dark{background:#111827;color:#fff}
.job .apply{position:absolute;right:18px;top:18px;font-size:9.5px;padding:7px 12px}
.job p{font-size:10.5px;color:var(--muted);margin-top:18px}
.meta{display:grid;grid-template-columns:185px 185px 1fr;margin-top:14px;font-size:9.5px;color:#374151}
.meta span{display:flex;align-items:center;gap:6px}
.req{font-size:9.5px;font-weight:500;margin-top:14px}
.req-list{display:flex;gap:14px;font-size:8px;margin-top:10px;color:#374151;font-weight:500}
.side{width:272px}
.side-card{border:1px solid var(--line);border-radius:10px;padding:16px 16px;box-shadow:0 2px 6px rgba(0,0,0,.04)}
.benefits{height:198px}
.benefits ul{list-style:none;margin-top:14px}
.benefits li{font-size:9.5px;line-height:23px;display:flex;align-items:center;gap:7px;color:#374151}
.quick{height:145px;margin-top:22px}
.quick p{font-size:9.5px;line-height:15px;color:var(--muted);margin-top:18px}

/* contact */
.contact{height:911px;background:var(--soft);padding-top:64px}
.contact-grid{display:flex;gap:29px;margin-top:70px}
.form-card{width:581px;height:577px;background:#fff;border:1px solid var(--line);border-radius:10px;padding:20px 18px}
.tabs{display:grid;grid-template-columns:repeat(3,1fr);gap:10px;margin-top:18px}
.tab{border:1px solid var(--line);border-radius:8px;height:44px;display:flex;flex-direction:column;align-items:center;justify-content:center;gap:5px;font-size:9.5px;font-weight:500}
.form-grid{display:grid;grid-template-columns:1fr 1fr;gap:18px 14px;margin-top:22px}
.fld label{font-size:9.5px;font-weight:500;display:block;margin-bottom:6px}
.input{height:26px;background:#f3f4f6;border-radius:6px;font-size:9px;color:#9ca3af;padding:0 10px;display:flex;align-items:center;justify-content:space-between}
.textarea{height:56px;align-items:flex-start;padding-top:7px}
.check{display:flex;align-items:center;gap:8px;font-size:9px;color:var(--muted);margin-top:20px}
.check i{width:10px;height:10px;background:#111827;border-radius:2px;display:block}
.send{width:100%;justify-content:center;margin-top:20px;padding:8px}
.cside{width:272px}
.info{height:321px;background:#fff}
.info-row{display:flex;gap:12px;margin-top:18px}
.info-row .ib{width:28px;height:28px;border-radius:6px;background:#eff6ff;color:var(--blue);display:flex;align-items:center;justify-content:center;flex-shrink:0}
.info-row b{font-size:10.5px;font-weight:500;display:block}
.info-row span{font-size:10px;display:block;margin-top:2px}
.info-row small{font-size:8px;color:var(--muted)}
.follow{height:146px;margin-top:21px;background:#fff}
.follow p{font-size:9.5px;line-height:15px;color:var(--muted);margin-top:22px}
.socials{display:flex;gap:6px;margin-top:10px}
.soc{background:var(--blue);color:#fff;font-size:8.5px;font-weight:500;border-radius:4px;padding:5px 7px}
.emergency{height:107px;margin-top:23px;background:#fef2f2;border-color:#fecaca}
.emergency h4{font-size:11px;font-weight:500;color:#991b1b}
.emergency p{font-size:9px;line-height:14px;color:#b91c1c;margin-top:12px}
.btn-red{background:var(--red);color:#fff;width:100%;justify-content:center;margin-top:8px;padding:7px}

/* footer */
.site-footer{height:654px;background:var(--navy);color:#cbd5e1;padding-top:70px}
.foot-top{display:flex}
.foot-brand{width:362px}
.foot-brand .brand{font-size:20px}
.foot-brand p{font-size:11px;line-height:19px;margin-top:36px;color:#cbd5e1}
.fcontact{font-size:9.5px;margin-top:20px;line-height:24px}
.fcontact div{display:flex;gap:8px;align-items:center}
.foot-soc{display:flex;gap:8px;margin-top:18px}
.foot-soc span{background:#1e2b52;color:#cbd5e1;font-size:8.5px;border-radius:4px;padding:6px 8px}
.fcol{width:181px;margin-top:-36px}
.fcol h4{color:#fff;font-size:11px;font-weight:600}
.fcol ul{list-style:none;margin-top:14px}
.fcol li{font-size:9.5px;line-height:20px;color:#94a3b8}
.fcerts{border-top:1px solid #1e2b52;margin-top:124px;padding-top:30px;text-align:center}
.fcerts h4{color:#fff;font-size:11px;font-weight:500;display:flex;align-items:center;gap:8px;justify-content:center}
.fbadges{display:grid;grid-template-columns:repeat(4,1fr);margin-top:24px;text-align:center}
.fb i{width:40px;height:40px;border-radius:50%;background:#1e2b52;display:block;margin:0 auto}
.fb b{display:block;color:var(--sky);font-size:10px;margin-top:10px}
.fb small{font-size:7.5px;color:#94a3b8}
.fbottom{border-top:1px solid #1e2b52;margin-top:34px;padding-top:16px;display:flex;justify-content:space-between;font-size:8.5px;color:#94a3b8}
.flinks{display:flex;gap:16px}
.fnote{text-align:center;font-size:7.5px;color:#64748b;margin-top:22px}
</style>
</head>
<body>

<header class="site-header">
  <div class="wrap">
    <div class="brand"><i></i>Harbor Crest</div>
    <nav class="nav"><span>Home</span><span>Services</span><span>Certifications</span><span>Careers</span><span>Contact</span></nav>
    <span class="btn btn-blue">Get Started</span>
  </div>
</header>

<section class="hero" role="img" aria-label="Hero banner with deep blue background representing business, technology and workforce">
  <div class="orb"></div>
  <div class="wrap">
    <span class="pill"><svg class="ic" style="width:11px;height:11px" viewBox="0 0 24 24"><path d="M12 3l7 3v6c0 4-3 7-7 9-4-2-7-5-7-9V6z"/></svg>Government Certified • VOSB • SDVOSB • DBE</span>
    <h1>Your Trusted Partner in <span>Workforce Solutions</span></h1>
    <p class="lead">Delivering exceptional staffing and workforce solutions across Healthcare, IT, Logistics, Maintenance, Construction, Manufacturing, and Industrial sectors for both private and government clients.</p>
    <div class="stats">
      <div class="stat"><b>500+</b><small>Projects Completed</small></div>
      <div class="stat"><b>10+</b><small>Years Experience</small></div>
      <div class="stat"><b>24/7</b><small>Support Available</small></div>
    </div>
    <div class="hero-cta">
      <span class="btn btn-blue">Discover Our Services <svg class="ic" style="width:11px;height:11px" viewBox="0 0 24 24"><path d="M5 12h14M13 6l6 6-6 6"/></svg></span>
      <span class="btn btn-white">Request Consultation</span>
    </div>
    <div class="hero-card">
      <div class="hc-head"><div class="hc-icon"><svg class="ic" viewBox="0 0 24 24"><rect x="4" y="4" width="16" height="16" rx="2"/><path d="M9 9h6M9 13h6"/></svg></div><div><b>Enterprise Solutions</b><small>Scalable workforce management</small></div></div>
      <div class="hc-row" style="margin-top:22px">Healthcare Staffing<i></i></div>
      <div class="hc-row">IT Solutions<i></i></div>
      <div class="hc-row">Government Contracts<i></i></div>
    </div>
  </div>
</section>

<section class="services">
  <div class="wrap">
    <div class="sec-head">
      <h2>Comprehensive Workforce Solutions</h2>
      <p>From healthcare to heavy industry, we provide skilled professionals across all major sectors, with specialized expertise in government contracting and compliance.</p>
    </div>
    <div class="svc-grid">
      <div class="svc"><div class="ico"><svg class="ic" viewBox="0 0 24 24"><path d="M12 20s-7-4.5-7-10a4 4 0 017-2.6A4 4 0 0119 10c0 5.5-7 10-7 10z"/></svg></div><h3>Healthcare</h3><p>Certified medical professionals, nurses, and healthcare support staff for hospitals and clinics.</p><ul><li>Licensed Professionals</li><li>Emergency Staffing</li><li>Long-term Placements</li></ul></div>
      <div class="svc"><div class="ico"><svg class="ic" viewBox="0 0 24 24"><rect x="3" y="4" width="18" height="12" rx="2"/><path d="M8 20h8M12 16v4"/></svg></div><h3>Information Technology</h3><p>Skilled IT professionals, developers, and technical specialists for digital transformation.</p><ul><li>Software Development</li><li>Cybersecurity</li><li>Cloud Solutions</li></ul></div>
      <div class="svc"><div class="ico"><svg class="ic" viewBox="0 0 24 24"><path d="M2 7h12v9H2zM14 10h4l3 3v3h-7"/><circle cx="6" cy="17" r="2"/><circle cx="17" cy="17" r="2"/></svg></div><h3>Logistics</h3><p>Supply chain experts, warehouse workers, and transportation professionals.</p><ul><li>Supply Chain Management</li><li>Warehouse Operations</li><li>Transportation</li></ul></div>
      <div class="svc"><div class="ico"><svg class="ic" viewBox="0 0 24 24"><path d="M14 6a4 4 0 005 5l-9 9-3-3 9-9a4 4 0 01-2-2z"/></svg></div><h3>Maintenance</h3><p>Experienced maintenance technicians and facilities management professionals.</p><ul><li>Preventive Maintenance</li><li>Emergency Repairs</li><li>Facilities Management</li></ul></div>
      <div class="svc r2"><div class="ico"><svg class="ic" viewBox="0 0 24 24"><path d="M4 17h16M6 17a6 6 0 0112 0M10 11V7h4v4"/></svg></div><h3>Construction</h3><p>Licensed contractors, project managers, and construction workers for all project sizes.</p><ul><li>Project Management</li><li>Skilled Trades</li><li>Safety Compliance</li></ul></div>
      <div class="svc r2"><div class="ico"><svg class="ic" viewBox="0 0 24 24"><path d="M4 20V8l5 3V8l5 3V4h6v16z"/></svg></div><h3>Manufacturing</h3><p>Production workers, quality control specialists, and manufacturing engineers.</p><ul><li>Production Line</li><li>Quality Assurance</li><li>Process Optimization</li></ul></div>
      <div class="svc r2"><div class="ico"><svg class="ic" viewBox="0 0 24 24"><circle cx="12" cy="12" r="3"/><circle cx="12" cy="12" r="8"/></svg></div><h3>Industrial</h3><p>Heavy industry professionals and specialized technical workers.</p><ul><li>Heavy Machinery</li><li>Safety Protocols</li><li>Technical Expertise</li></ul></div>
      <div class="svc r2"><div class="ico"><svg class="ic" viewBox="0 0 24 24"><circle cx="9" cy="8" r="3"/><path d="M3 20a6 6 0 0112 0M16 5a3 3 0 010 6M21 20a6 6 0 00-4-5.6"/></svg></div><h3>General Labor</h3><p>Reliable general laborers for temporary and permanent positions across industries.</p><ul><li>Flexible Scheduling</li><li>Background Verified</li><li>Immediate Availability</li></ul></div>
    </div>
    <div class="gov-banner">
      <h3>Government Contracting Expertise</h3>
      <p>As a certified VOSB, SDVOSB, DBE, and Minority-Owned Business, we specialize in government contracts and understand the unique requirements of federal, state, and local agencies.</p>
      <span class="btn btn-white">View Our Capabilities <svg class="ic" style="width:11px;height:11px" viewBox="0 0 24 24"><path d="M5 12h14M13 6l6 6-6 6"/></svg></span>
    </div>
  </div>
</section>

<section class="gov">
  <div class="wrap">
    <div class="sec-head">
      <span class="pill tag"><svg class="ic" style="width:11px;height:11px" viewBox="0 0 24 24"><path d="M12 3l7 3v6c0 4-3 7-7 9-4-2-7-5-7-9V6z"/></svg>Government Certified</span>
      <h2 style="margin-top:24px">Certified Government Contractor</h2>
      <p>Our certifications demonstrate our commitment to excellence and compliance in government contracting, ensuring seamless partnership with federal, state, and local agencies.</p>
    </div>
    <div class="cert-grid">
      <div class="cert"><div class="ico"><svg class="ic" viewBox="0 0 24 24"><path d="M12 3l7 3v6c0 4-3 7-7 9-4-2-7-5-7-9V6z"/></svg></div><span class="badge b-green">VOSB Certified</span><h3>Veteran-Owned Small Business</h3><p>Officially certified veteran-owned business with proven track record in government contracting.</p></div>
      <div class="cert"><div class="ico"><svg class="ic" viewBox="0 0 24 24"><path d="M12 3l2.7 5.6 6.1.8-4.4 4.3 1 6.1L12 17l-5.4 2.8 1-6.1L3.2 9.4l6.1-.8z"/></svg></div><span class="badge b-blue">SDVOSB Certified</span><h3>Service-Disabled Veteran-Owned Small Business</h3><p>Specialized certification recognizing our service-disabled veteran leadership and commitment.</p></div>
      <div class="cert"><div class="ico"><svg class="ic" viewBox="0 0 24 24"><rect x="5" y="3" width="14" height="18" rx="1"/><path d="M9 7h2M13 7h2M9 11h2M13 11h2M10 21v-4h4v4"/></svg></div><span class="badge b-purple">DBE Certified</span><h3>Disadvantaged Business Enterprise</h3><p>Certified DBE status enabling participation in federally funded transportation projects.</p></div>
      <div class="cert"><div class="ico"><svg class="ic" viewBox="0 0 24 24"><circle cx="9" cy="8" r="3"/><path d="M3 20a6 6 0 0112 0M16 5a3 3 0 010 6M21 20a6 6 0 00-4-5.6"/></svg></div><span class="badge b-orange">Minority-Owned Business</span><h3>Certified Minority Business Enterprise</h3><p>Recognized minority-owned business with expertise in diverse workforce solutions.</p></div>
    </div>
    <div class="gov-low">
      <div class="core">
        <div class="panel-title"><svg class="ic" style="color:var(--green)" viewBox="0 0 24 24"><circle cx="12" cy="12" r="9"/><path d="M8 12l3 3 5-6"/></svg>Core Capabilities</div>
        <ul class="core-list">
          <li>Federal Government Contracting</li><li>State &amp; Local Government Projects</li>
          <li>Prime &amp; Subcontracting Opportunities</li><li>Small Business Set-Aside Programs</li>
          <li>Emergency Response Staffing</li><li>Compliance &amp; Documentation</li>
          <li>Security Clearance Personnel</li><li>Competitive Pricing Models</li>
        </ul>
      </div>
      <div class="capab">
        <div class="panel-title"><svg class="ic" style="color:var(--blue)" viewBox="0 0 24 24"><path d="M6 3h9l4 4v14H6z"/><path d="M9 12h7M9 16h7"/></svg>Capability Statement</div>
        <p>Download our comprehensive capability statement detailing our certifications, past performance, and core competencies for government contracting.</p>
        <div class="doc"><div><b>HCS Capability Statement 2025</b><small>PDF • 2.4 MB • Updated Jan 2025</small></div><span class="btn btn-blue"><svg class="ic" style="width:10px;height:10px" viewBox="0 0 24 24"><path d="M12 4v12M6 11l6 6 6-6M4 20h16"/></svg>Download</span></div>
        <div class="doc"><div><b>GSA Schedule Information</b><small>PDF • 1.8 MB • Updated Dec 2024</small></div><span class="btn btn-ghost"><svg class="ic" style="width:10px;height:10px" viewBox="0 0 24 24"><path d="M12 4v12M6 11l6 6 6-6M4 20h16"/></svg>Download</span></div>
        <span class="btn btn-blue full">Request Custom Proposal</span>
      </div>
    </div>
  </div>
</section>

<section class="careers">
  <div class="wrap">
    <div class="sec-head">
      <span class="pill tag-green"><svg class="ic" style="width:11px;height:11px" viewBox="0 0 24 24"><circle cx="9" cy="8" r="3"/><path d="M3 20a6 6 0 0112 0"/></svg>Join Our Team</span>
      <h2 style="margin-top:16px">Build Your Career with HCS</h2>
      <p>Join a team that values professional growth, diversity, and excellence. We offer competitive benefits and opportunities across multiple industries.</p>
    </div>
    <div class="careers-grid">
      <div class="jobs">
        <div class="search"><div class="field"><svg class="ic" style="width:10px;height:10px" viewBox="0 0 24 24"><circle cx="11" cy="11" r="6"/><path d="M20 20l-4-4"/></svg>Search jobs...</div><span class="filter"><svg class="ic" style="width:10px;height:10px" viewBox="0 0 24 24"><path d="M4 5h16l-6 7v6l-4 2v-8z"/></svg>Filter</span></div>

        <div class="job">
          <h3>Senior IT Systems Administrator</h3>
          <div class="chips"><span class="chip">Information Technology</span><span class="chip dark">Senior</span></div>
          <span class="btn btn-blue apply">Apply Now</span>
          <p>Manage and maintain critical IT infrastructure for government clients. Security clearance required.</p>
          <div class="meta"><span><svg class="ic" style="width:10px;height:10px" viewBox="0 0 24 24"><path d="M12 21s-6-6-6-11a6 6 0 0112 0c0 5-6 11-6 11z"/></svg>Washington, DC</span><span><svg class="ic" style="width:10px;height:10px" viewBox="0 0 24 24"><circle cx="12" cy="12" r="8"/><path d="M12 8v4l3 2"/></svg>Full-time</span><span>$ &nbsp;$85,000 - $110,000</span></div>
          <div class="req">Requirements:</div>
          <div class="req-list"><span>5+ years experience</span><span>Security Clearance</span><span>Windows/Linux</span><span>VMware</span></div>
        </div>

        <div class="job">
          <h3>Registered Nurse - ICU</h3>
          <div class="chips"><span class="chip">Healthcare</span><span class="chip">Experienced</span></div>
          <span class="btn btn-blue apply">Apply Now</span>
          <p>Provide critical care nursing services in intensive care units across partner healthcare facilities.</p>
          <div class="meta"><span><svg class="ic" style="width:10px;height:10px" viewBox="0 0 24 24"><path d="M12 21s-6-6-6-11a6 6 0 0112 0c0 5-6 11-6 11z"/></svg>Multiple Locations</span><span><svg class="ic" style="width:10px;height:10px" viewBox="0 0 24 24"><circle cx="12" cy="12" r="8"/><path d="M12 8v4l3 2"/></svg>Contract</span><span>$ &nbsp;$40 - $65/hour</span></div>
          <div class="req">Requirements:</div>
          <div class="req-list"><span>RN License</span><span>ICU Experience</span><span>BLS/ACLS</span><span>2+ years experience</span></div>
        </div>

        <div class="job">
          <h3>Construction Project Manager</h3>
          <div class="chips"><span class="chip">Construction</span><span class="chip dark">Senior</span></div>
          <span class="btn btn-blue apply">Apply Now</span>
          <p>Lead construction projects for government facilities. PMP certification preferred.</p>
          <div class="meta"><span><svg class="ic" style="width:10px;height:10px" viewBox="0 0 24 24"><path d="M12 21s-6-6-6-11a6 6 0 0112 0c0 5-6 11-6 11z"/></svg>Virginia Beach, VA</span><span><svg class="ic" style="width:10px;height:10px" viewBox="0 0 24 24"><circle cx="12" cy="12" r="8"/><path d="M12 8v4l3 2"/></svg>Full-time</span><span>$ &nbsp;$75,000 - $95,000</span></div>
          <div class="req">Requirements:</div>
          <div class="req-list"><span>Project Management</span><span>Construction Experience</span><span>Government Projects</span><span>PMP Preferred</span></div>
        </div>

        <div class="job">
          <h3>Warehouse Operations Supervisor</h3>
          <div class="chips"><span class="chip">Logistics</span><span class="chip">Mid-level</span></div>
          <span class="btn btn-blue apply">Apply Now</span>
          <p>Supervise warehouse operations and ensure efficient logistics processes.</p>
          <div class="meta"><span><svg class="ic" style="width:10px;height:10px" viewBox="0 0 24 24"><path d="M12 21s-6-6-6-11a6 6 0 0112 0c0 5-6 11-6 11z"/></svg>Atlanta, GA</span><span><svg class="ic" style="width:10px;height:10px" viewBox="0 0 24 24"><circle cx="12" cy="12" r="8"/><path d="M12 8v4l3 2"/></svg>Full-time</span><span>$ &nbsp;$55,000 - $68,000</span></div>
          <div class="req">Requirements:</div>
          <div class="req-list"><span>Warehouse Management</span><span>Team Leadership</span><span>Logistics Experience</span><span>WMS Systems</span></div>
        </div>
      </div>

      <aside class="side">
        <div class="side-card benefits">
          <div class="panel-title"><svg class="ic" style="color:#eab308" viewBox="0 0 24 24"><path d="M12 3l2.7 5.6 6.1.8-4.4 4.3 1 6.1L12 17l-5.4 2.8 1-6.1L3.2 9.4l6.1-.8z"/></svg>Employee Benefits</div>
          <ul>
            <li><svg class="ic" style="width:11px;height:11px;color:var(--green)" viewBox="0 0 24 24"><circle cx="12" cy="12" r="9"/><path d="M8 12l3 3 5-6"/></svg>Competitive Salary &amp; Benefits</li>
            <li><svg class="ic" style="width:11px;height:11px;color:var(--green)" viewBox="0 0 24 24"><circle cx="12" cy="12" r="9"/><path d="M8 12l3 3 5-6"/></svg>Health, Dental &amp; Vision Insurance</li>
            <li><svg class="ic" style="width:11px;height:11px;color:var(--green)" viewBox="0 0 24 24"><circle cx="12" cy="12" r="9"/><path d="M8 12l3 3 5-6"/></svg>401(k) with Company Match</li>
            <li><svg class="ic" style="width:11px;height:11px;color:var(--green)" viewBox="0 0 24 24"><circle cx="12" cy="12" r="9"/><path d="M8 12l3 3 5-6"/></svg>Professional Development</li>
            <li><svg class="ic" style="width:11px;height:11px;color:var(--green)" viewBox="0 0 24 24"><circle cx="12" cy="12" r="9"/><path d="M8 12l3 3 5-6"/></svg>Flexible Work Arrangements</li>
            <li><svg class="ic" style="width:11px;height:11px;color:var(--green)" viewBox="0 0 24 24"><circle cx="12" cy="12" r="9"/><path d="M8 12l3 3 5-6"/></svg>Career Advancement Opportunities</li>
          </ul>
        </div>
        <div class="side-card quick">
          <div class="panel-title">Quick Application</div>
          <p>Don't see the perfect role? Submit your information and we'll contact you when relevant positions become available.</p>
          <span class="btn btn-blue full" style="margin-top:10px;padding:6px">Submit General Application</span>
        </div>
      </aside>
    </div>
  </div>
</section>

<section class="contact">
  <div class="wrap">
    <div class="sec-head">
      <span class="pill tag"><svg class="ic" style="width:11px;height:11px" viewBox="0 0 24 24"><path d="M4 5h16v11H9l-5 4z"/></svg>Get In Touch</span>
      <h2 style="margin-top:16px">Ready to Partner with HCS?</h2>
      <p>Let's discuss how our certified workforce solutions can help your organization achieve its goals. Contact us today for a free consultation.</p>
    </div>
    <div class="contact-grid">
      <div class="form-card">
        <div class="panel-title"><svg class="ic" style="color:var(--blue)" viewBox="0 0 24 24"><rect x="4" y="4" width="16" height="16" rx="2"/><path d="M9 9h6M9 13h6"/></svg>Request a Consultation</div>
        <div class="tabs">
          <div class="tab"><svg class="ic" style="width:11px;height:11px" viewBox="0 0 24 24"><circle cx="12" cy="8" r="3"/><path d="M6 20a6 6 0 0112 0"/></svg>Staffing Needs</div>
          <div class="tab"><svg class="ic" style="width:11px;height:11px" viewBox="0 0 24 24"><rect x="5" y="3" width="14" height="18" rx="1"/><path d="M10 21v-4h4v4"/></svg>Government Contract</div>
          <div class="tab"><svg class="ic" style="width:11px;height:11px" viewBox="0 0 24 24"><path d="M4 5h16v11H9l-5 4z"/></svg>General Inquiry</div>
        </div>
        <div class="form-grid">
          <div class="fld"><label>First Name *</label><div class="input">Enter your first name</div></div>
          <div class="fld"><label>Last Name *</label><div class="input">Enter your last name</div></div>
          <div class="fld"><label>Email Address *</label><div class="input">Enter your email</div></div>
          <div class="fld"><label>Phone Number</label><div class="input">Enter your phone number</div></div>
          <div class="fld"><label>Company/Organization</label><div class="input">Enter company name</div></div>
          <div class="fld"><label>Service Interest</label><div class="input">Select a service <span>⌄</span></div></div>
          <div class="fld" style="grid-column:1/3"><label>Project Details</label><div class="input textarea">Please describe your staffing needs, project timeline, and any specific requirements...</div></div>
        </div>
        <div class="check"><i></i>I'd like to receive updates about HCS services and industry insights</div>
        <span class="btn btn-blue send"><svg class="ic" style="width:11px;height:11px" viewBox="0 0 24 24"><path d="M21 3L10 14M21 3l-7 18-4-7-7-4z"/></svg>Send Message</span>
      </div>

      <aside class="cside">
        <div class="side-card info">
          <div class="panel-title">Contact Information</div>
          <div class="info-row"><div class="ib"><svg class="ic" style="width:13px;height:13px" viewBox="0 0 24 24"><path d="M5 4h4l2 5-2.5 1.5a11 11 0 005 5L15 13l5 2v4a2 2 0 01-2 2A16 16 0 013 6a2 2 0 012-2z"/></svg></div><div><b>Phone</b><span>+1 (555) 123-4567</span><small>24/7 Emergency Support</small></div></div>
          <div class="info-row"><div class="ib"><svg class="ic" style="width:13px;height:13px" viewBox="0 0 24 24"><rect x="3" y="5" width="18" height="14" rx="2"/><path d="M3 7l9 6 9-6"/></svg></div><div><b>Email</b><span>contact@harborcrest.example</span><small>Response within 24 hours</small></div></div>
          <div class="info-row"><div class="ib"><svg class="ic" style="width:13px;height:13px" viewBox="0 0 24 24"><path d="M12 21s-6-6-6-11a6 6 0 0112 0c0 5-6 11-6 11z"/><circle cx="12" cy="10" r="2"/></svg></div><div><b>Address</b><span>1234 Commerce Park Dr</span><small>Suite 100, Washington, DC 20001</small></div></div>
          <div class="info-row"><div class="ib"><svg class="ic" style="width:13px;height:13px" viewBox="0 0 24 24"><circle cx="12" cy="12" r="8"/><path d="M12 8v4l3 2"/></svg></div><div><b>Business Hours</b><span>Mon - Fri: 8:00 AM - 6:00 PM</span><small>Weekend emergency support available</small></div></div>
        </div>
        <div class="side-card follow">
          <div class="panel-title">Follow Us</div>
          <p>Stay connected for industry insights, job opportunities, and company updates.</p>
          <div class="socials"><span class="soc">Workvine</span><span class="soc">Quillo</span><span class="soc">Pagebloom</span></div>
        </div>
        <div class="side-card emergency">
          <h4>24/7 Emergency Support</h4>
          <p>For urgent staffing needs or emergency situations, contact our 24/7 hotline.</p>
          <span class="btn btn-red"><svg class="ic" style="width:10px;height:10px" viewBox="0 0 24 24"><path d="M5 4h4l2 5-2.5 1.5a11 11 0 005 5L15 13l5 2v4a2 2 0 01-2 2A16 16 0 013 6a2 2 0 012-2z"/></svg>Call Emergency Line</span>
        </div>
      </aside>
    </div>
  </div>
</section>

<footer class="site-footer">
  <div class="wrap">
    <div class="foot-top">
      <div class="foot-brand">
        <div class="brand"><i></i>Harbor Crest</div>
        <p>A certified VOSB, SDVOSB, DBE, and Minority-Owned Business specializing in workforce solutions across Healthcare, IT, Logistics, Construction, Manufacturing, and Industrial sectors for government and private clients.</p>
        <div class="fcontact">
          <div><svg class="ic" style="width:10px;height:10px;color:var(--sky)" viewBox="0 0 24 24"><path d="M5 4h4l2 5-2.5 1.5a11 11 0 005 5L15 13l5 2v4a2 2 0 01-2 2A16 16 0 013 6a2 2 0 012-2z"/></svg>+1 (555) 123-4567</div>
          <div><svg class="ic" style="width:10px;height:10px;color:var(--sky)" viewBox="0 0 24 24"><rect x="3" y="5" width="18" height="14" rx="2"/><path d="M3 7l9 6 9-6"/></svg>contact@harborcrest.example</div>
          <div><svg class="ic" style="width:10px;height:10px;color:var(--sky)" viewBox="0 0 24 24"><path d="M12 21s-6-6-6-11a6 6 0 0112 0c0 5-6 11-6 11z"/></svg>Washington, DC 20001</div>
        </div>
        <div class="foot-soc"><span>Workvine</span><span>Quillo</span><span>Pagebloom</span></div>
      </div>
      <div class="fcol"><h4>Services</h4><ul><li>Healthcare Staffing</li><li>IT Solutions</li><li>Logistics Support</li><li>Maintenance Services</li><li>Construction Projects</li><li>Manufacturing Support</li></ul></div>
      <div class="fcol"><h4>Company</h4><ul><li>About HCS</li><li>Our Leadership</li><li>Certifications</li><li>Case Studies</li><li>News &amp; Updates</li><li>Contact Us</li></ul></div>
      <div class="fcol"><h4>Resources</h4><ul><li>Capability Statement</li><li>GSA Schedule</li><li>Safety Resources</li><li>Compliance Guide</li><li>Industry Insights</li><li>Career Resources</li></ul></div>
    </div>
    <div class="fcerts">
      <h4><svg class="ic" style="width:12px;height:12px;color:var(--sky)" viewBox="0 0 24 24"><path d="M12 3l7 3v6c0 4-3 7-7 9-4-2-7-5-7-9V6z"/></svg>Government Certifications</h4>
      <div class="fbadges">
        <div class="fb"><i></i><b>VOSB</b><small>Veteran-Owned Small Business</small></div>
        <div class="fb"><i></i><b>SDVOSB</b><small>Service-Disabled Veteran-Owned Small Business</small></div>
        <div class="fb"><i></i><b>DBE</b><small>Disadvantaged Business Enterprise</small></div>
        <div class="fb"><i></i><b>MBE</b><small>Minority Business Enterprise</small></div>
      </div>
    </div>
    <div class="fbottom">
      <span>© 2025 Harbor Crest Solutions. All rights reserved.</span>
      <div class="flinks"><span>Privacy Policy</span><span>Terms of Service</span><span>Equal Opportunity</span><span>Vendor Registration</span><span>Supplier Diversity</span><span>Accessibility</span></div>
    </div>
    <div class="fnote">HCS is an Equal Opportunity Employer committed to workforce diversity. We comply with all federal, state, and local employment laws and regulations.</div>
  </div>
</footer>

</body>
</html>
```